Business Card Design for Telecommunications and IT Solutions company "OKRA"

BC for telecommunications company name "OKRA" with slogan "Telecom & IT Solutions"

should have the full name as above "OKRA" and the slogan
color reqiured black, red (dark) and white

simple, professional, serious, modern design is required

1 side of business card have a full details, contacts and logo
other side have only the logo, website and full company name "ALOKRA Company for Telecommunications service & Information Technology LLC"

i have attached the logo and current business card sample and note that the logo was changed not the same in the attached business card

Industry/Entity Type

Telecommunications

Contact Information for Business Card

Full name: Omar Nabil Al Hudari
Job title: General Manager
Mobile no: +964xxxxxxxxx
email: omar@okra-tel.example
full name of the company: ALOKRA Company Telecommunications Services & Information Technology LLC.
website: www.okra-tel.example
address: Nakheel Dist. 148/7 JubailaQadim, Basra, Iraq

Requirements
Must have
• two languages in the same side of business card (English, Arabic) for only the name and title

```html
<!DOCTYPE html>
<html lang="en">
<head>
<meta charset="utf-8">
<title>OKRA Business Card</title>
<link rel="stylesheet" href="https://fonts.googleapis.com/css2?family=Open+Sans:wght@400;600;700&family=Noto+Naskh+Arabic:wght@400;600&family=Tinos&display=swap">
<style>
  :root {
    --bg: #e9e7e4;
    --card: #ffffff;
    --card-edge: #f1f1f1;
    --red: #c8202a;
    --ink: #1c1c1c;
    --grey: #555555;
    --rule: #3a3a3a;
  }
  * { box-sizing: border-box; margin: 0; padding: 0; }
  html, body { width: 1200px; height: 885px; overflow: hidden; }
  body {
    background: var(--bg);
    font-family: "Open Sans", Arial, sans-serif;
    color: var(--ink);
    position: relative;
  }
  .card {
    position: absolute;
    left: 250px;
    width: 700px;
    height: 400px;
    border-radius: 22px;
    background: linear-gradient(135deg, var(--card) 0%, var(--card) 55%, var(--card-edge) 100%);
    box-shadow: 0 6px 18px rgba(0,0,0,0.18);
    overflow: hidden;
  }
  .card--front { top: 28px; }
  .card--back { top: 457px; }

  .brand { display: flex; align-items: center; gap: 10px; }
  .brand__dot { width: 14px; height: 14px; border-radius: 50%; background: var(--red); }
  .brand__name { font-weight: 700; color: var(--red); letter-spacing: 1px; line-height: 1; }
  .slogan { font-family: "Tinos", "Times New Roman", serif; color: var(--grey); }

  /* front */
  .front__brand { position: absolute; left: 58px; top: 58px; }
  .front__brand .brand__name { font-size: 50px; }
  .front__brand .slogan { font-size: 14px; margin-top: 8px; margin-left: 24px; }

  .person__ar-name { position: absolute; right: 48px; top: 30px; font-family: "Noto Naskh Arabic", serif; font-size: 26px; font-weight: 600; direction: rtl; line-height: 1.3; }
  .person__ar-title { position: absolute; right: 48px; top: 72px; font-family: "Noto Naskh Arabic", serif; font-size: 15px; line-height: 1.3; color: var(--grey); direction: rtl; }
  .person__name { position: absolute; right: 48px; top: 124px; font-size: 25px; font-weight: 600; line-height: 34px; }
  .person__rule { position: absolute; left: 56px; right: 48px; top: 168px; height: 1px; background: var(--rule); }
  .person__title { position: absolute; right: 48px; top: 176px; font-size: 17px; line-height: 24px; color: var(--grey); }

  .address { position: absolute; right: 48px; top: 238px; text-align: right; font-size: 19px; line-height: 1.45; font-style: normal; }

  .contacts { position: absolute; left: 58px; bottom: 38px; list-style: none; font-size: 17px; line-height: 1.55; }
  .contacts li { display: flex; align-items: center; gap: 12px; }
  .contacts .icon { width: 20px; height: 20px; background: var(--red); border-radius: 3px; display: flex; align-items: center; justify-content: center; }

  /* back */
  .back__inner { position: absolute; inset: 0; display: flex; flex-direction: column; align-items: center; justify-content: center; text-align: center; }
  .back__inner .brand__name { font-size: 70px; }
  .back__inner .slogan { font-size: 16px; margin-top: 12px; }
  .company { font-size: 32px; font-weight: 400; margin-top: 34px; letter-spacing: 0.5px; }
  .company-full { font-size: 16px; color: var(--grey); margin-top: 8px; }
  .back__web { font-size: 15px; color: var(--grey); margin-top: 22px; }
</style>
</head>
<body>

<section class="card card--front">
  <div class="front__brand">
    <div class="brand"><span class="brand__dot"></span><span class="brand__name">OKRA</span></div>
    <p class="slogan">Telecom &amp; IT Solutions</p>
  </div>

  <p class="person__ar-name">عمر نبيل الحضري</p>
  <p class="person__ar-title">المدير المفوض</p>
  <p class="person__name">Omar Nabil Al Hudari</p>
  <div class="person__rule"></div>
  <p class="person__title">General Manager</p>

  <address class="address">
    Nakheel Dist. 148/7<br>
    JubailaQadim, Basra, Iraq
  </address>

  <ul class="contacts">
    <li>
      <span class="icon"><svg width="12" height="12" viewBox="0 0 24 24"><path fill="#fff" d="M6.6 10.8a15 15 0 0 0 6.6 6.6l2.2-2.2c.3-.3.7-.4 1-.2 1.1.4 2.3.6 3.6.6.6 0 1 .4 1 1V20c0 .6-.4 1-1 1A17 17 0 0 1 3 4c0-.6.4-1 1-1h3.5c.6 0 1 .4 1 1 0 1.3.2 2.5.6 3.6.1.3 0 .7-.2 1z"/></svg></span>
      +964xxxxxxxxx
    </li>
    <li>
      <span class="icon"><svg width="12" height="10" viewBox="0 0 24 18"><rect x="1" y="1" width="22" height="16" fill="none" stroke="#fff" stroke-width="2"/><path d="M1 1l11 9 11-9" fill="none" stroke="#fff" stroke-width="2"/></svg></span>
      omar@okra-tel.example
    </li>
    <li>
      <span class="icon"><svg width="12" height="12" viewBox="0 0 24 24" fill="none" stroke="#fff" stroke-width="2"><circle cx="12" cy="12" r="10"/><ellipse cx="12" cy="12" rx="4" ry="10"/><path d="M2 12h20"/></svg></span>
      www.okra-tel.example
    </li>
  </ul>
</section>

<section class="card card--back">
  <div class="back__inner">
    <div class="brand"><span class="brand__dot"></span><span class="brand__name">OKRA</span></div>
    <p class="slogan">Telecom &amp; IT Solutions</p>
    <p class="company">ALOKRA Company</p>
    <p class="company-full">Telecommunications Services &amp; Information Technology LLC.</p>
    <p class="back__web">www.okra-tel.example</p>
  </div>
</section>

</body>
</html>
```